Orthodontist Needs Promotional Discount Postcard

5.5 x 8.5 Horizontal 2-Sided Postcard for mailing.
Images & Logo on both sides okay; must be free stock Images from legit sources only, or use attached images. See our website for information, CoveLineSmiles.com
Context to include:
New Patient Special $500 off Braces or Clear Aligners
Cannot be combined with any other discounts.
Major dental insurance plans and Vita-Plan accepted
Affordable payment options are available
Call to schedule your free consultation
Present this new patient offer to receive your discount.
Offer ends January 31, 2022.
805-419-2276 www. CoveLineSmiles.com
462 N. Marigold Street, Suite B, Ventura, CA 93001-5812
office@covelinesmiles.com

```html
<!DOCTYPE html>
<html lang="en">
<head>
<meta charset="utf-8">
<title>Cove Line Smiles – New Patient Postcard</title>
<link href="https://fonts.googleapis.com/css2?family=Lato:wght@300;400;700;900&display=swap" rel="stylesheet">
<style>
:root{
  --blue:#29a8e0;
  --green:#7dc86e;
  --teal:#6fd3c0;
  --mint:#e2f5ec;
  --ink:#2e2e2e;
  --grey:#666;
  --page:#efefef;
}
*{box-sizing:border-box;margin:0;padding:0}
html,body{width:707px;height:1200px;overflow:hidden}
body{background:var(--page);font-family:'Lato',sans-serif;color:var(--ink);position:relative}
.card{position:absolute;left:24px;width:660px;height:429px;background:#fff;overflow:hidden;box-shadow:0 2px 4px rgba(0,0,0,.25)}
.card--offer{top:150px}
.card--welcome{top:620px;background:var(--mint)}
.abs{position:absolute}
.bg{position:absolute;inset:0;width:660px;height:429px}
.photo{position:absolute;border-radius:50%;border:3px solid #fff}
/* offer side */
.badge-green{left:35px;top:28px;width:120px;height:120px;border-radius:50%;background:var(--green);border:5px solid #fff;box-shadow:0 4px 8px rgba(0,0,0,.15);color:#fff;text-align:center;padding-top:30px}
.badge-green .big{font-size:14px;line-height:17px;font-weight:400}
.badge-green .small{font-size:7.5px;line-height:9px;margin-top:2px}
.badge-teal{left:144px;top:54px;width:72px;height:72px;border-radius:50%;background:var(--teal);border:3px solid var(--blue);color:#fff;font-size:26px;font-weight:700;text-align:center;line-height:66px}
.badge-teal sup{font-size:12px;vertical-align:14px}
.photo--aligner{left:220px;top:48px;width:108px;height:108px;border-color:var(--blue);background:radial-gradient(circle at 45% 40%,#fbf7f2 0 25%,#e9a59c 45%,#b95d58 80%)}
.offer-lines{left:30px;top:164px;width:310px;text-align:center}
.offer-lines .note{font-size:12px;font-weight:400}
.offer-lines .deadline{font-size:20px;font-weight:700;color:var(--blue);line-height:24px}
.schedule{left:35px;top:236px}
.schedule .lead{font-size:12.5px;font-weight:300;color:var(--grey)}
.schedule .free{font-size:16.5px;font-weight:900;line-height:18px}
.schedule .free span{color:var(--green);font-weight:700}
.phone-line{left:35px;top:282px;display:flex;align-items:center;gap:8px;font-size:14px;color:var(--grey)}
.ico{width:16px;height:16px;border:1.3px solid var(--green);border-radius:50%;display:flex;align-items:center;justify-content:center}
.location-label{left:37px;top:315px;font-size:8px;font-weight:900;display:flex;align-items:center;gap:8px}
.location-label i{display:block;width:80px;height:2px;background:var(--green)}
.map{left:0;top:329px;width:208px;height:86px;background:linear-gradient(135deg,#f4f6f4,#e3e7e6 60%,#cfe8f3)}
.photo--robot{left:218px;top:231px;width:110px;height:110px;border:2px solid var(--blue);background:radial-gradient(circle at 50% 45%,#ffffff 0 20%,#d8dadc 60%,#b9bcbf)}
.planning{left:213px;top:352px;width:122px;text-align:center}
.planning h3{font-size:8px;font-weight:900;color:var(--ink)}
.planning h3 span{color:var(--green);font-weight:700}
.planning p{font-size:7px;line-height:9.5px;color:var(--grey);margin-top:4px}
.brand-stack{left:420px;top:20px;width:160px;text-align:center}
.brand-dot{width:42px;height:42px;border-radius:50%;background:var(--blue);margin:0 auto 6px}
.brand-name{font-size:18px;font-weight:400;color:var(--blue);letter-spacing:.5px;white-space:nowrap}
.stamp{left:570px;top:123px;width:55px;height:54px;border:2px solid #bbb}
.address-box{left:351px;top:206px;width:273px;height:150px;border:1.5px solid #e1e1e1;border-radius:6px}
/* welcome side */
.brand-row{left:20px;top:32px;display:flex;align-items:center;gap:7px}
.brand-row .brand-dot{margin:0;width:38px;height:38px}
.brand-row .brand-name{font-size:17px;letter-spacing:.3px}
.photo--team{left:16px;top:95px;width:204px;height:140px;border-radius:0;border:none;background:linear-gradient(160deg,#cfd6dc,#9aa6ae 55%,#c77a86)}
.welcome{left:281px;top:15px;color:#fff}
.welcome h1{font-size:47px;font-weight:900;line-height:48px;letter-spacing:.5px}
.welcome h2{font-size:27px;font-weight:900;line-height:28px}
.tagline{display:inline-block;margin-top:6px;padding:2px 8px;font-size:10px;border:1px dashed var(--teal)}
.photo--braces{left:252px;top:128px;width:118px;height:118px;border-color:var(--teal);background:radial-gradient(circle at 50% 50%,#fbf7f3 0 22%,#e9918d 50%,#c9605f)}
.photo--mirror{left:373px;top:141px;width:116px;height:116px;border-color:var(--teal);background:radial-gradient(circle at 55% 50%,#fdfbf9 0 25%,#ef8f90 55%,#d06a6d)}
.photo--smile{left:490px;top:94px;width:148px;height:148px;border-color:var(--teal);background:radial-gradient(circle at 50% 55%,#fcfaf8 0 22%,#e79e94 52%,#efd1c7)}
.treatment{left:20px;top:253px}
.treatment h3{font-size:15px;font-weight:700;color:var(--blue)}
.treatment .doc{font-size:13px;color:#444}
.treatment .cred{font-size:7.5px;color:var(--grey)}
.features{left:20px;top:314px;display:grid;grid-template-columns:158px 140px;row-gap:12px;font-size:10px;color:#333}
.features li{list-style:none;display:flex;align-items:center;gap:6px}
.features .ico{width:20px;height:20px;border:1.5px solid var(--teal)}
.plans{left:370px;top:276px;width:270px;height:75px;background:var(--green);border-radius:8px;color:#fff;text-align:center;overflow:hidden}
.plans h3{font-size:17px;font-weight:900;background:var(--blue);margin-top:8px;line-height:20px}
.plans p{font-size:11px;line-height:14px;margin-top:4px}
.contact-now{left:20px;top:392px;font-size:16px;color:#fff;font-weight:400}
.call{left:257px;top:381px;color:#fff;text-align:left}
.call b{display:inline-block;background:#fff;color:var(--blue);font-size:11px;font-weight:900;padding:0 9px;line-height:12px;clip-path:polygon(0 0,100% 0,85% 100%,0 100%)}
.call small{display:block;font-size:7px;font-weight:700}
.info{color:#fff;font-size:7.3px;display:flex;align-items:center;gap:6px}
.info svg{flex:none}
</style>
</head>
<body>

<section class="card card--offer" aria-label="Postcard offer side">
  <svg class="bg" viewBox="0 0 660 429" aria-hidden="true">
    <path d="M0,0H660V60C600,20 520,8 430,30C330,55 250,90 150,118C90,134 40,130 0,128Z" fill="var(--blue)"/>
    <path d="M0,429V415C260,420 520,400 660,345V429Z" fill="var(--blue)"/>
  </svg>

  <div class="abs badge-green">
    <div class="big">NEW PATIENT<br>SPECIAL</div>
    <div class="small">Off Braces or Clear<br>Aligners</div>
  </div>
  <div class="abs badge-teal"><sup>$</sup>500</div>
  <div class="photo photo--aligner" role="img" aria-label="Close-up photo of a smile with a clear aligner"></div>

  <div class="abs offer-lines">
    <p class="note">Present this new patient offer to receive your discount.</p>
    <p class="deadline">OFFER ENDS JANUARY 31, 2022</p>
    <p class="note">Cannot combined with any other disounts</p>
  </div>

  <div class="abs schedule">
    <p class="lead">CALL TO SCHEDULE YOUR</p>
    <p class="free">FREE <span>CONSULTATION</span></p>
  </div>
  <div class="abs phone-line">
    <span class="ico"><svg width="9" height="9" viewBox="0 0 24 24"><path d="M6.6 10.8a15 15 0 006.6 6.6l2.2-2.2c.3-.3.7-.4 1-.2 1.1.4 2.3.6 3.6.6.6 0 1 .4 1 1V20c0 .6-.4 1-1 1A17 17 0 013 4c0-.6.4-1 1-1h3.5c.6 0 1 .4 1 1 0 1.3.2 2.5.6 3.6.1.3 0 .7-.2 1z" fill="var(--green)"/></svg></span>
    805-419-2276
  </div>

  <div class="abs location-label">OUR LOCATION <i></i></div>
  <div class="abs map" role="img" aria-label="Street map showing the practice location in Ventura"></div>

  <div class="photo photo--robot" role="img" aria-label="Photo of a robotic arm used for treatment planning"></div>
  <div class="abs planning">
    <h3>3D <span>TREATMENT PLANNING</span></h3>
    <p>True 3D diagnosis allows us to get all parts of your teeth in the correct position Including the roots.</p>
  </div>

  <div class="abs brand-stack">
    <div class="brand-dot"></div>
    <div class="brand-name">Cove Line Smiles</div>
  </div>
  <div class="abs stamp"></div>
  <div class="abs address-box"></div>
</section>

<section class="card card--welcome" aria-label="Postcard welcome side">
  <svg class="bg" viewBox="0 0 660 429" aria-hidden="true">
    <path d="M272,0H660V150C540,160 420,200 300,232C200,258 90,248 0,236V222C110,212 190,160 222,80C234,36 252,12 272,0Z" fill="var(--blue)"/>
    <path d="M0,236C90,248 200,258 300,232C420,200 540,160 660,150V429H0Z" fill="#fff"/>
    <path d="M230,238C360,210 520,160 660,165" stroke="var(--mint)" stroke-width="8" fill="none"/>
    <path d="M0,372C200,385 420,340 660,300V429H0Z" fill="var(--blue)"/>
  </svg>

  <div class="abs brand-row">
    <div class="brand-dot"></div>
    <div class="brand-name">Cove Line Smiles</div>
  </div>
  <div class="photo photo--team" role="img" aria-label="Photo of two orthodontists in masks with a smiling patient"></div>

  <div class="abs welcome">
    <h1>WELCOME</h1>
    <h2>COVE LINE SMILES</h2>
    <span class="tagline">Superior Technology Developed Right Here</span>
  </div>

  <div class="photo photo--braces" role="img" aria-label="Close-up photo of teeth with metal braces"></div>
  <div class="photo photo--mirror" role="img" aria-label="Close-up photo of teeth with a dental mirror"></div>
  <div class="photo photo--smile" role="img" aria-label="Close-up photo of a hand fitting a clear aligner"></div>

  <div class="abs treatment">
    <h3>ORTHODONTIC TREATMENT</h3>
    <p class="doc">Daniel R. Whitford, DDS, MS</p>
    <p class="cred">Certified Orthodontic Specialist</p>
  </div>

  <ul class="abs features">
    <li><span class="ico"><svg width="10" height="10" viewBox="0 0 10 10"><path d="M2 5l2 2 4-4" stroke="var(--teal)" stroke-width="1.4" fill="none"/></svg></span>3D Diagnosis</li>
    <li><span class="ico"><svg width="10" height="10" viewBox="0 0 10 10"><path d="M2 5l2 2 4-4" stroke="var(--teal)" stroke-width="1.4" fill="none"/></svg></span>Robotic Assistance</li>
    <li><span class="ico"><svg width="10" height="10" viewBox="0 0 10 10"><path d="M2 5l2 2 4-4" stroke="var(--teal)" stroke-width="1.4" fill="none"/></svg></span>Virtual Appointments</li>
    <li><span class="ico"><svg width="10" height="10" viewBox="0 0 10 10"><path d="M2 5l2 2 4-4" stroke="var(--teal)" stroke-width="1.4" fill="none"/></svg></span>Advanced Brackets</li>
  </ul>

  <div class="abs plans">
    <h3>MAJOR DENTAL PLANS</h3>
    <p>Dental insurance plans &amp; Vita-Plan accepted<br>Affordable payment options are available</p>
  </div>

  <div class="abs contact-now">CONTACT NOW</div>
  <div class="abs call"><b>CALL</b><small>Dr. WHITFORD Today!</small></div>

  <div class="abs info" style="left:359px;top:376px">
    <svg width="10" height="8" viewBox="0 0 10 8"><rect width="10" height="8" fill="#fff"/><path d="M0 0l5 4 5-4" stroke="var(--blue)" fill="none"/></svg>
    office@covelinesmiles.com
  </div>
  <div class="abs info" style="left:359px;top:402px">
    <svg width="9" height="9" viewBox="0 0 24 24"><path d="M6.6 10.8a15 15 0 006.6 6.6l2.2-2.2c.3-.3.7-.4 1-.2 1.1.4 2.3.6 3.6.6.6 0 1 .4 1 1V20c0 .6-.4 1-1 1A17 17 0 013 4c0-.6.4-1 1-1h3.5c.6 0 1 .4 1 1 0 1.3.2 2.5.6 3.6.1.3 0 .7-.2 1z" fill="#fff"/></svg>
    805-419-2276
  </div>
  <div class="abs info" style="left:517px;top:369px;line-height:9px">
    <svg width="9" height="11" viewBox="0 0 9 11"><path d="M4.5 0A4 4 0 00.5 4c0 3 4 7 4 7s4-4 4-7a4 4 0 00-4-4z" fill="#fff"/><circle cx="4.5" cy="4" r="1.5" fill="var(--blue)"/></svg>
    <span>462 N. Marigold Street, Suite<br>B, Ventura, CA 93001-5812</span>
  </div>
  <div class="abs info" style="left:517px;top:402px">
    <svg width="9" height="9" viewBox="0 0 10 10"><circle cx="5" cy="5" r="4.3" stroke="#fff" fill="none"/><path d="M1 5h8M5 .7c-2 2.5-2 6.1 0 8.6M5 .7c2 2.5 2 6.1 0 8.6" stroke="#fff" fill="none" stroke-width=".8"/></svg>
    www. CoveLineSmiles.com
  </div>
</section>

</body>
</html>
```